Website for Torvel Capital - investment banking firm

We have a corporate identity (thanks to Ranjita/41238) and want to extend that into a website design.  See the attached zipped files.
We have software folks in-house to do the coding.
See the attached Project Brief & Notes for more details.  Don't worry about the actual text - lorem ipsum will be fine.
The server will be Apache.
Thank you!
Desmond

```html
<!DOCTYPE html>
<html lang="en">
<head>
<meta charset="utf-8">
<title>Torvel Capital</title>
<link href="https://fonts.googleapis.com/css2?family=Montserrat:wght@700&family=Open+Sans:ital,wght@0,400;0,600;0,700;1,400&family=Libre+Baskerville&display=swap" rel="stylesheet">
<style>
:root{
  --navy:#1d4585;
  --blue:#2563b0;
  --ink:#333;
  --muted:#8a8a8a;
  --line:#e2e2e2;
  --dark:#1e1f22;
  --darker:#141516;
  --white:#fff;
  --bar-bg:#e9eef5;
}
*{box-sizing:border-box;margin:0;padding:0}
html,body{width:1200px;height:4149px;overflow:hidden}
body{font-family:"Open Sans",Arial,sans-serif;color:var(--ink);background:var(--white);font-size:14px}
section,header,footer{position:relative;width:1200px}
.section-title{font-size:26px;font-weight:400;letter-spacing:1px;color:#444;text-align:center}
.section-title b{color:var(--blue);font-weight:700}
.section-rule{width:60px;height:2px;background:var(--blue);margin:10px auto 0}
.section-sub{font-size:12px;color:var(--muted);text-align:center;margin-top:14px}
.btn{display:inline-block;background:var(--navy);color:var(--white);font-size:11px;font-weight:600;padding:8px 18px;letter-spacing:.5px}

/* header */
.site-header{height:86px}
.brand{font-family:"Libre Baskerville",Georgia,serif;font-size:26px;color:var(--navy);position:absolute;left:54px;top:24px}
.socials-top{position:absolute;right:40px;top:8px;display:flex;gap:8px}
.socials-top span{width:18px;height:18px;border-radius:50%;background:#9aa7b8}
.main-nav{position:absolute;right:40px;top:58px;display:flex;gap:22px;font-family:"Libre Baskerville",Georgia,serif;font-size:12px;color:#333}
.main-nav .active{color:var(--navy);border-bottom:2px solid var(--navy);padding-bottom:4px}

/* hero */
.hero{height:490px;background:linear-gradient(180deg,#9aa3a9 0%,#6f7a82 45%,#4d5660 100%);display:flex;flex-direction:column;align-items:center;justify-content:center}
.hero-title{font-family:"Montserrat",Arial,sans-serif;font-size:50px;letter-spacing:6px;color:var(--white);text-align:center;line-height:58px;margin-top:-20px}
.hero .btn{margin-top:18px;padding:5px 14px;font-size:9px}

/* services */
.services{height:554px;padding-top:60px}
.service-grid{display:flex;justify-content:center;gap:110px;margin-top:48px}
.service{width:220px;text-align:center}
.service svg{width:74px;height:74px}
.service h3{font-size:15px;font-weight:700;margin:18px 0 8px}
.service p{font-size:11px;color:var(--muted);line-height:17px}
.service .btn{margin-top:16px}
.divider{width:420px;height:1px;background:var(--line);position:absolute;left:390px;bottom:30px}

/* about */
.about{height:358px;padding-top:10px}
.about-body{display:flex;gap:60px;padding:0 90px;margin-top:46px}
.about-text{width:540px}
.tabs{display:flex;gap:18px;font-size:10px;color:#555;border-bottom:1px solid var(--line);padding-bottom:6px}
.tabs .active{color:var(--blue);border-bottom:3px solid var(--blue);padding-bottom:4px;margin-bottom:-7px}
.about-text p{font-size:11px;color:var(--muted);line-height:17px;margin-top:16px}
.capabilities{width:400px;margin-top:-16px}
.capabilities h4{font-size:12px;font-weight:600;margin-bottom:12px}
.bar{display:flex;align-items:center;height:18px;background:var(--bar-bg);margin-bottom:14px;position:relative}
.bar-fill{height:100%;background:var(--navy);color:var(--white);font-size:9px;padding-left:10px;line-height:18px}
.bar-val{position:absolute;right:8px;font-size:9px;color:#555}

/* stats */
.stats{height:254px;background:linear-gradient(90deg,#2a2d33 0%,#3c4148 50%,#2b2e34 100%);display:flex;justify-content:center;gap:150px;align-items:center;margin-top:8px}
.stat{text-align:center;color:var(--white)}
.stat-icon{width:46px;height:46px;border-radius:50%;background:var(--navy);margin:0 auto 10px;display:flex;align-items:center;justify-content:center}
.stat-num{font-size:30px}
.stat-label{font-size:20px}

/* team */
.team{height:596px;padding-top:52px}
.team-grid{display:flex;justify-content:center;gap:26px;margin-top:30px}
.member{width:226px;text-align:center}
.member-photo{width:226px;height:222px}
.member h3{font-size:15px;font-weight:700;margin-top:20px}
.member .role{font-size:10px;color:#555;margin-top:4px}
.member p{font-size:11px;color:var(--muted);line-height:16px;margin-top:8px;padding:0 14px}

/* testimonial */
.testimonial{height:266px;background:linear-gradient(180deg,#3a3f47,#23262b);text-align:center;padding-top:48px}
.quote-icon{width:46px;height:46px;border-radius:50%;background:var(--navy);margin:0 auto;display:flex;align-items:center;justify-content:center;color:var(--white);font-size:26px;font-weight:700}
.testimonial p{font-style:italic;color:var(--white);font-size:18px;margin-top:26px}
.dots{display:flex;justify-content:center;gap:6px;margin-top:28px}
.dots span{width:6px;height:6px;border-radius:50%;background:#777}
.dots .on{background:var(--white)}
.partners{height:125px;background:var(--darker);display:flex;justify-content:center;align-items:center;gap:86px}
.partner{width:70px;height:70px;border-radius:50%;background:#3a5aa8}
.partner.alt{border-radius:4px;background:#2d7ab8}

/* features */
.features{height:547px;padding-top:56px}
.feature-grid{display:grid;grid-template-columns:repeat(3,230px);column-gap:90px;row-gap:60px;justify-content:center;margin-top:50px}
.feature h3{display:flex;align-items:center;gap:8px;font-size:15px;font-weight:700}
.feature p{font-size:11px;color:var(--muted);line-height:16px;margin-top:8px;padding-left:28px}

/* contact */
.contact-head{height:108px;padding-top:8px}
.contact-band{height:250px;background:linear-gradient(90deg,#202327,#3d424a 60%,#272a2f);display:flex;justify-content:center;gap:150px;align-items:center}
.contact-item{text-align:center;color:var(--white);width:160px}
.contact-item h3{font-size:18px;font-weight:700;margin-top:4px}
.contact-item .value{font-size:15px;margin-top:2px;white-space:nowrap}
.contact-form{height:303px;display:flex;justify-content:center;gap:30px;padding-top:34px}
.form-fields{display:flex;flex-direction:column;gap:12px;width:310px}
.field{height:34px;border:1px solid var(--line);font-size:10px;color:#888;padding:10px}
.field.message{width:310px;height:130px}
.contact-form .btn{position:absolute;left:510px;top:200px}
.to-top{position:absolute;left:579px;top:250px;width:30px;height:30px;background:var(--dark);display:flex;align-items:center;justify-content:center}

/* footer */
.site-footer{height:191px;background:var(--dark);color:var(--white);text-align:center;padding-top:44px}
.site-footer h2{font-size:22px;font-weight:700;letter-spacing:1px}
.site-footer small{display:block;font-size:11px;color:#aaa;margin-top:10px}
.socials-foot{display:flex;justify-content:center;gap:10px;margin-top:14px}
.socials-foot span{width:24px;height:24px;border-radius:50%;border:1px solid var(--white)}
</style>
</head>
<body>

<header class="site-header">
  <div class="brand">Torvel Capital</div>
  <div class="socials-top"><span></span><span></span><span></span><span></span></div>
  <nav class="main-nav">
    <span class="active">Home</span><span>About</span><span>Services</span><span>Current Engagements</span><span>Completed Transactions</span>
  </nav>
</header>

<section class="hero" role="img" aria-label="Photo of businessmen in an office">
  <h1 class="hero-title">LOREM IPSUM IS<br>SIMPLY</h1>
  <span class="btn">GET STARTED</span>
</section>

<section class="services">
  <h2 class="section-title">OUR <b>SERVICES</b></h2>
  <div class="section-rule"></div>
  <div class="service-grid">
    <div class="service">
      <svg viewBox="0 0 74 74" fill="none" stroke="#111" stroke-width="5"><path d="M37 6 L64 16 V36 C64 52 52 63 37 69 C22 63 10 52 10 36 V16 Z"/><path d="M24 37 L34 47 L52 27"/></svg>
      <h3>Lorem Ipsum</h3>
      <p>Lorem Ipsum is simply dummy text of the printing and typesetting industry. Lorem Ipsum has been the industry's standard dummy text ever since the 1500s.</p>
      <span class="btn">VIEW MORE</span>
    </div>
    <div class="service">
      <svg viewBox="0 0 74 74" fill="none" stroke="#111" stroke-width="4" stroke-linejoin="round"><path d="M68 6 L6 32 L30 42 L40 68 Z"/><path d="M68 6 L30 42"/></svg>
      <h3>Lorem Ipsum</h3>
      <p>Lorem Ipsum is simply dummy text of the printing and typesetting industry. Lorem Ipsum has been the industry's standard dummy text ever since the 1500s.</p>
      <span class="btn">VIEW MORE</span>
    </div>
    <div class="service">
      <svg viewBox="0 0 74 74"><path d="M4 10 H16 L26 50 H62 L70 20 H20" fill="none" stroke="#111" stroke-width="5"/><rect x="22" y="22" width="44" height="26" fill="#111"/><circle cx="30" cy="62" r="6" fill="#111"/><circle cx="58" cy="62" r="6" fill="#111"/></svg>
      <h3>Lorem Ipsum</h3>
      <p>Lorem Ipsum is simply dummy text of the printing and typesetting industry. Lorem Ipsum has been the industry's standard dummy text ever since the 1500s.</p>
      <span class="btn">VIEW MORE</span>
    </div>
  </div>
  <div class="divider"></div>
</section>

<section class="about">
  <h2 class="section-title">ABOUT <b>US</b></h2>
  <div class="section-rule"></div>
  <p class="section-sub">Lorem Ipsum is simply dummy text of the printing and typesetting industry.</p>
  <div class="about-body">
    <div class="about-text">
      <div class="tabs"><span class="active">Philosophy</span><span>History</span><span>Knowledge</span><span>Experience</span></div>
      <p>Lorem ipsum dolor sit amet, consectetur adipiscing elit. Vivamus lacus mi, facilisis sit amet lacinia at, dictum non mauris. Sed sodales ultrices nunc vel pharetra. Nullam sed aliquet nibh, eget cursus lacus. Nam volutpat ante ac est rhoncus, ac pretium lectus tincidunt. Fusce vitae nibh lorem, volutpat ipsum. Cras ultricies pretium mi at facilisis.</p>
    </div>
    <div class="capabilities">
      <h4>Our Capabilities</h4>
      <div class="bar"><div class="bar-fill" style="width:73%">Lorem Ipsum</div><span class="bar-val">73%</span></div>
      <div class="bar"><div class="bar-fill" style="width:53%">Lorem Ipsum</div><span class="bar-val">53%</span></div>
      <div class="bar"><div class="bar-fill" style="width:90%">Lorem Ipsum</div><span class="bar-val">90%</span></div>
      <div class="bar"><div class="bar-fill" style="width:94%">Lorem Ipsum</div><span class="bar-val">94%</span></div>
    </div>
  </div>
</section>

<section class="stats" role="img" aria-label="Dark photo of a smiling businessman">
  <div class="stat"><div class="stat-icon"><svg width="20" height="20" viewBox="0 0 20 20" fill="#fff"><path d="M10 1a6 6 0 0 0-6 6c0 5 6 12 6 12s6-7 6-12a6 6 0 0 0-6-6z"/></svg></div><div class="stat-num">46</div><div class="stat-label">Lorem Ipsum</div></div>
  <div class="stat"><div class="stat-icon"><svg width="20" height="20" viewBox="0 0 20 20" fill="#fff"><path d="M19 1 L1 9 L9 11 L11 19 Z"/></svg></div><div class="stat-num">79</div><div class="stat-label">Lorem Ipsum</div></div>
  <div class="stat"><div class="stat-icon"><svg width="22" height="20" viewBox="0 0 22 20" fill="#fff"><path d="M4 8 L6 3 H16 L18 8 H20 V15 H2 V8 Z"/><circle cx="6" cy="16" r="2"/><circle cx="16" cy="16" r="2"/></svg></div><div class="stat-num">34</div><div class="stat-label">Lorem Ipsum</div></div>
  <div class="stat"><div class="stat-icon"><svg width="20" height="20" viewBox="0 0 20 20" fill="#fff"><rect x="3" y="2" width="14" height="16" rx="1"/></svg></div><div class="stat-num">127</div><div class="stat-label">Lorem Ipsum</div></div>
</section>

<section class="team">
  <h2 class="section-title">OUR <b>TEAM</b></h2>
  <div class="section-rule"></div>
  <p class="section-sub">Lorem Ipsum is simply dummy text of the printing and typesetting industry.</p>
  <div class="team-grid">
    <div class="member"><div class="member-photo" role="img" aria-label="Portrait of a red-haired team member" style="background:linear-gradient(#f1e4dc,#c98a6a)"></div><h3>Lorem Ipsum</h3><div class="role">Lorem Ipsum</div><p>Lorem Ipsum is simply dummy text of the printing and typesetting industry. Lorem Ipsum has been</p></div>
    <div class="member"><div class="member-photo" role="img" aria-label="Portrait of a team member in a white shirt" style="background:linear-gradient(#eeeeee,#b9aea6)"></div><h3>Lorem Ipsum</h3><div class="role">Lorem Ipsum</div><p>Lorem Ipsum is simply dummy text of the printing and typesetting industry. Lorem Ipsum has been</p></div>
    <div class="member"><div class="member-photo" role="img" aria-label="Portrait of a blonde team member" style="background:linear-gradient(#f2ece4,#cfa77a)"></div><h3>Lorem Ipsum</h3><div class="role">Lorem Ipsum</div><p>Lorem Ipsum is simply dummy text of the printing and typesetting industry. Lorem Ipsum has been</p></div>
    <div class="member"><div class="member-photo" role="img" aria-label="Portrait of a team member in a suit" style="background:linear-gradient(#eeeeee,#4a3a34)"></div><h3>Lorem Ipsum</h3><div class="role">Lorem Ipsum</div><p>Lorem Ipsum is simply dummy text of the printing and typesetting industry. Lorem Ipsum has been</p></div>
  </div>
</section>

<section class="testimonial" role="img" aria-label="Dark photo of city buildings">
  <div class="quote-icon">&ldquo;</div>
  <p>Lorem Ipsum is simply dummy text of the printing and typesetting industry. Lorem Ipsum has been</p>
  <div class="dots"><span class="on"></span><span></span></div>
</section>
<section class="partners" aria-label="Partner badges">
  <span class="partner"></span><span class="partner alt"></span><span class="partner"></span><span class="partner alt"></span><span class="partner"></span><span class="partner alt"></span><span class="partner"></span>
</section>

<section class="features">
  <h2 class="section-title">MORE <b>FEATURES</b></h2>
  <div class="section-rule"></div>
  <p class="section-sub">Lorem ipsum dolor sit amet, consectetur adipiscing elit, sed do eiusmod tempor.</p>
  <div class="feature-grid">
    <div class="feature"><h3><svg width="18" height="18" viewBox="0 0 18 18" fill="#222"><rect x="2" y="2" width="14" height="10"/><rect x="6" y="13" width="6" height="3"/></svg>Lorem Ipsum</h3><p>Lorem Ipsum is simply dummy text of the printing and typesetting industry. Lorem Ipsum has been the.</p></div>
    <div class="feature"><h3><svg width="20" height="18" viewBox="0 0 20 18" fill="none" stroke="#222" stroke-width="2"><path d="M6 4 L1 9 L6 14 M14 4 L19 9 L14 14 M12 2 L8 16"/></svg>Lorem Ipsum</h3><p>Lorem Ipsum is simply dummy text of the printing and typesetting industry. Lorem Ipsum has been the.</p></div>
    <div class="feature"><h3><svg width="14" height="18" viewBox="0 0 14 18" fill="none" stroke="#222" stroke-width="2"><rect x="2" y="1" width="10" height="16" rx="1"/></svg>Lorem Ipsum</h3><p>Lorem Ipsum is simply dummy text of the printing and typesetting industry. Lorem Ipsum has been the.</p></div>
    <div class="feature"><h3><svg width="18" height="18" viewBox="0 0 18 18" stroke="#222" stroke-width="3"><path d="M3 15 L15 3"/></svg>Lorem Ipsum</h3><p>Lorem Ipsum is simply dummy text of the printing and typesetting industry. Lorem Ipsum has been the.</p></div>
    <div class="feature"><h3><svg width="20" height="18" viewBox="0 0 20 18" fill="none" stroke="#222" stroke-width="2"><rect x="1" y="2" width="18" height="14"/><path d="M3 14 L8 8 L12 12 L15 9 L18 13"/></svg>Lorem Ipsum</h3><p>Lorem Ipsum is simply dummy text of the printing and typesetting industry. Lorem Ipsum has been the.</p></div>
    <div class="feature"><h3><svg width="16" height="18" viewBox="0 0 16 18" fill="none" stroke="#222" stroke-width="2"><path d="M2 1 H10 L14 5 V17 H2 Z M5 9 H11 M5 13 H11"/></svg>Lorem Ipsum</h3><p>Lorem Ipsum is simply dummy text of the printing and typesetting industry. Lorem Ipsum has been the.</p></div>
  </div>
</section>

<section class="contact-head">
  <h2 class="section-title">CONTACT <b>US</b></h2>
  <div class="section-rule"></div>
  <p class="section-sub">Lorem Ipsum is simply dummy text of the printing and typesetting industry.</p>
</section>
<section class="contact-band" role="img" aria-label="Dark photo of a modern building facade">
  <div class="contact-item"><div class="stat-icon"><svg width="20" height="20" viewBox="0 0 20 20" fill="#fff"><path d="M10 1a6 6 0 0 0-6 6c0 5 6 12 6 12s6-7 6-12a6 6 0 0 0-6-6z"/></svg></div><h3>Address</h3><div class="value">Lorem Ipsum Is</div></div>
  <div class="contact-item"><div class="stat-icon"><svg width="20" height="20" viewBox="0 0 20 20" fill="#fff"><path d="M19 1 L1 9 L9 11 L11 19 Z"/></svg></div><h3>Phone</h3><div class="value">123456789</div></div>
  <div class="contact-item"><div class="stat-icon"><svg width="22" height="20" viewBox="0 0 22 20" fill="#fff"><path d="M4 8 L6 3 H16 L18 8 H20 V15 H2 V8 Z"/><circle cx="6" cy="16" r="2"/><circle cx="16" cy="16" r="2"/></svg></div><h3>Email</h3><div class="value">Lorem@Lorem.com</div></div>
  <div class="contact-item"><div class="stat-icon"><svg width="20" height="20" viewBox="0 0 20 20" fill="#fff"><rect x="3" y="2" width="14" height="16" rx="1"/></svg></div><h3>Web</h3><div class="value">hello@torvelcapital.com</div></div>
</section>

<section class="contact-form">
  <div class="form-fields">
    <div class="field">Name</div>
    <div class="field">Email</div>
    <div class="field">Subject</div>
  </div>
  <div class="field message">Message</div>
  <span class="btn">SEND MESSAGE</span>
  <span class="to-top"><svg width="14" height="14" viewBox="0 0 14 14" fill="#fff"><path d="M7 2 L13 10 H1 Z"/></svg></span>
</section>

<footer class="site-footer">
  <h2>NORVAN</h2>
  <small>All Rights Reserved. Copyright 2016</small>
  <div class="socials-foot"><span></span><span></span><span></span><span></span></div>
</footer>

</body>
</html>
```